Wealth Management Business Card

We are a professional services consulting firm that specializes in high net worth individuals over $25,000,000, executives C-suite and above, closely held businesses owners, family offices and highly compensated employees.

Our focus is on risk mitigation and tax efficient strategies. Our clients take their risk on themselves and have a proven track record generating wealth. Our directive is to preserve and protect the wealth they’ve already created.

Our company Harbridge Advisory is geared around five directives of asset protection:
1) Legal Structuring
2) Leverage & Financing
3) Risk Management - Asset Protection & Insurance, Trustee Work
4) Asset Management & Investing - Under www.qelvantcapital.com
5) Tax Efficient Strategies

Our Company Mark is a Pentagon with a key in the middle. A pentagon is the most efficient defensive structure. Each point of a pentagon is equal distance front every point . Each side provides support to another and works together, which is the key to our clients success.

Our key colors are blue, black and silver.

We ‘re located in the Pacific Northwest with bi coastal and international clients. We have fewer, higher net worth clients and provide exceptional customer service. We do not do social media.

website is www.harbridgepath.com

Target Market(s)

High End Clients

Contact Information for Business Card

extra thick

Font styles to use
Serif

Requirements
Must have
• Metalic foil for lettering.
Black Background on one side
White Background on the other
Horizontal Format Only
No Rounded corners
Not Marketing sales information on the card.
Nice to have
• imprinted texture on the card
Should not have
• lots of color

```html
<!DOCTYPE html>
<html lang="en">
<head>
<meta charset="utf-8">
<title>Harbridge Advisory — Business Card</title>
<link href="https://fonts.googleapis.com/css2?family=Cinzel:wght@600&family=Montserrat:wght@500&display=swap" rel="stylesheet">
<style>
  :root {
    --stage: #c8c8c8;
    --navy-deep: #0d0c33;
    --navy-mid: #1b1656;
    --foil: #f3efe0;
    --ink-navy: #0b2466;
    --paper-left: #eef0f2;
    --paper-right: #d2d2d4;
    --divider: #efe6c8;
    --text-grey: #666a70;
    --label-grey: #4d4f55;
  }
  * { margin: 0; padding: 0; box-sizing: border-box; }
  html, body { width: 1027px; height: 1200px; overflow: hidden; background: var(--stage); }
  .canvas { position: relative; width: 1027px; height: 1200px; }

  .card-front {
    position: absolute; left: 131px; top: 106px; width: 753px; height: 496px;
    background: radial-gradient(ellipse at 50% 25%, var(--navy-mid) 0%, #15124a 45%, var(--navy-deep) 100%);
    overflow: hidden;
  }
  .front-name {
    position: absolute; left: 0; width: 100%; top: 230px;
    text-align: center; font-family: "Cinzel", serif; font-weight: 600;
    font-size: 44px; line-height: 50px; letter-spacing: 2px; color: var(--foil);
  }
  .front-rule {
    position: absolute; left: 0; top: 412px; width: 100%; height: 1px; background: var(--foil);
  }
  .front-rule-bar {
    position: absolute; left: 278px; top: 410px; width: 197px; height: 5px;
    border-radius: 3px; background: var(--foil);
  }

  .card-back {
    position: absolute; left: 131px; top: 633px; width: 753px; height: 464px;
    border-radius: 6px; overflow: hidden; display: flex;
  }
  .back-brand {
    width: 359px; height: 100%; background: var(--paper-left); position: relative;
  }
  .back-divider { width: 2px; height: 100%; background: var(--divider); }
  .back-details {
    flex: 1; height: 100%; background: linear-gradient(135deg, #dcdcde, var(--paper-right));
    position: relative;
  }
  .back-name {
    position: absolute; left: 0; width: 100%; top: 115px; text-align: center;
    font-family: "Cinzel", serif; font-weight: 600; font-size: 38px; line-height: 44px;
    letter-spacing: 1px; color: var(--ink-navy);
  }
  .holder-name {
    position: absolute; left: 50px; top: 108px;
    font-family: "Cinzel", serif; font-weight: 600; font-size: 40px; color: var(--ink-navy);
  }
  .holder-role {
    position: absolute; left: 52px; top: 160px;
    font-family: "Montserrat", sans-serif; font-weight: 500; font-size: 16px;
    letter-spacing: 7px; color: var(--label-grey);
  }
  .contact-list { position: absolute; left: 34px; top: 240px; list-style: none; }
  .contact-item {
    display: flex; align-items: center; height: 36px;
    font-family: "Montserrat", sans-serif; font-weight: 500; font-size: 16.5px; color: var(--text-grey);
  }
  .contact-icon { width: 20px; height: 20px; margin-right: 14px; fill: var(--ink-navy); }
</style>
</head>
<body>
<div class="canvas">
  <section class="card-front" role="img" aria-label="Dark navy card face with subtle chevron texture">
    <div class="front-name">HARBRIDGE<br>ADVISORY</div>
    <div class="front-rule"></div>
    <div class="front-rule-bar"></div>
  </section>

  <section class="card-back">
    <div class="back-brand">
      <div class="back-name">HARBRIDGE<br>ADVISORY</div>
    </div>
    <div class="back-divider"></div>
    <div class="back-details">
      <div class="holder-name">YOUR NAME</div>
      <div class="holder-role">POSITION</div>
      <ul class="contact-list">
        <li class="contact-item">
          <svg class="contact-icon" viewBox="0 0 20 20"><path d="M10 1a6 6 0 0 0-6 6c0 4.5 6 12 6 12s6-7.5 6-12a6 6 0 0 0-6-6zm0 8.3A2.3 2.3 0 1 1 10 4.7a2.3 2.3 0 0 1 0 4.6z"/></svg>
          804 Lorem Street, City Name
        </li>
        <li class="contact-item">
          <svg class="contact-icon" viewBox="0 0 20 20"><path d="M2 5h16v10H2z M2 5l8 6 8-6" fill="none" stroke="#0b2466" stroke-width="1.8"/></svg>
          yourname@yourlogo.com
        </li>
        <li class="contact-item">
          <svg class="contact-icon" viewBox="0 0 20 20"><path d="M15.5 3.5l-2.2 2.8 1.2 1.6c-1.2 2.6-3.3 4.8-5.9 6.1l-1.6-1.2-2.8 2.2c.7 1.2 1.8 1.8 3 1.6 4.8-1 8.6-4.9 9.5-9.7.2-1.3-.3-2.6-1.2-3.4z"/></svg>
          (123) 456 789
        </li>
        <li class="contact-item">
          <svg class="contact-icon" viewBox="0 0 20 20"><g fill="none" stroke="#0b2466" stroke-width="1.4"><circle cx="10" cy="10" r="8"/><ellipse cx="10" cy="10" rx="3.5" ry="8"/><path d="M2 10h16M3.2 6h13.6M3.2 14h13.6M10 2v16"/></g></svg>
          yourlogo.com
        </li>
      </ul>
    </div>
  </section>
</div>
</body>
</html>
```